Retail Consultant Business Card Design

We're looking to update the look of our very old business cards. We work primarily in the fast paced retail industry, and would like a business card that won't look dated after a few years.

We are consultants that focus primarily on shopping malls (80%), or mixed use developments (20% shopping + office space + residential). That being the case, we know that there is a lot of room for creativity. We are not a law firm, so the design doesn't have to be very static or serious. We are also not a clothing brand, so it shouldn't be too "out there" (lipstick font, jean jacket background....etc).

We're looking for something more "middle of the road", with the design leaning more towards the creative side. Our consulting firm is not very big, so we are very open to breaking away from the "traditional" or simple business card model.

One last thing that might help you, is to know who we generally hand these cards out to. It really ranges from Developers to Architects, to actual retail brands like Vela, K&T, Brentwick, Tug & Fox, Lumira...etc.

Contact Information for Business Card

Company Name: (Horizon Venture Methods Worldwide, LLC)
Individuals Name & Title
Company Address: (382 W. Alder Lane, Suite C, Tustin, CA 92781)
Telephone Number: (714) 555-0182
Fax Number: (714) 555-0147
Website: hvmworld.example
Email

Font styles to use
Serif

Colors

Designer to choose colors to be used in the design.

Requirements
Must have
• 1. The incorporation of our logo in whatever way you think would work. We have no requirements for how this should happen.
• 2. Space in the back for a QR Code, with space for instructions like
• "save us as a contact on your mobile" (or something to that effect). This will allow our clients to scan the information on the card into their phones for quick contact creation. Obviously we will handle the whole QR Code issue, but if you could mock it up , so that we could get a sense of how it would look.
• 3. Try and use brighter colors, instead of darker ones. This is really up to you, the darker colors might make other colors pop. I just mention this, because we are trying to give the sense of energy or movement, if that makes any sense.
• 4. Obviously, space for all the normal business card text (Company name, person name, phone number, email.....etc)

```html
<!DOCTYPE html>
<html lang="en">
<head>
<meta charset="utf-8">
<title>Horizon Venture Methods Worldwide — Business Card</title>
<link rel="stylesheet" href="https://fonts.googleapis.com/css2?family=Lato:wght@400;700&family=Noto+Serif:wght@400&display=swap">
<style>
  :root {
    --backdrop: #3b3c40;
    --card-white: #ffffff;
    --card-shade: #e4e5e7;
    --card-dark: #232325;
    --ink: #2a2a2a;
    --ink-light: #d9d9db;
    --brand-blue: #1a73c4;
    --rule-blue: #4a9ad8;
    --faint-blue: #cfe8f7;
    --mark-blue: #2a8fd3;
  }
  * { margin: 0; padding: 0; box-sizing: border-box; }
  html, body {
    width: 1200px; height: 900px; overflow: hidden;
    background: var(--backdrop);
  }
  .card {
    position: absolute; left: 250px;
    width: 700px; height: 400px;
    border-radius: 22px; overflow: hidden;
    box-shadow: 0 10px 30px rgba(0,0,0,0.35);
  }

  /* Front */
  .card--front {
    top: 40px;
    background: radial-gradient(ellipse at 70% 65%, var(--card-white) 35%, var(--card-shade) 100%);
  }
  .faint-mark {
    position: absolute; left: 313px; top: 73px;
    width: 267px; height: 267px; border-radius: 50%;
    background: var(--faint-blue); opacity: 0.55;
  }
  .brand {
    position: absolute; left: 40px; top: 34px;
    display: flex; align-items: center; gap: 18px;
  }
  .brand-dot {
    width: 64px; height: 64px; border-radius: 50%;
    background: var(--mark-blue);
  }
  .brand-name {
    font-family: "Noto Serif", serif; font-size: 17px; font-weight: 400;
    line-height: 1.3; color: var(--ink);
  }
  .person {
    position: absolute; left: 40px; top: 132px;
  }
  .person-name {
    font-family: "Noto Serif", serif; font-size: 31px; font-weight: 400;
    color: var(--brand-blue); line-height: 1.1;
  }
  .person-title {
    font-family: "Lato", sans-serif; font-size: 16px;
    color: var(--ink); margin-top: 3px;
  }
  .divider {
    position: absolute; left: 133px; top: 190px;
    width: 527px; height: 1.5px; background: var(--rule-blue);
  }
  .contacts {
    position: absolute; left: 40px; top: 218px;
    list-style: none;
    font-family: "Lato", sans-serif; font-size: 15px; color: var(--ink);
  }
  .contacts li { display: flex; align-items: center; gap: 10px; height: 25px; }
  .contacts svg { width: 11px; height: 11px; fill: var(--brand-blue); }
  .contacts .web-domain { color: var(--brand-blue); }
  .address {
    position: absolute; right: 40px; bottom: 32px; text-align: right;
    font-family: "Lato", sans-serif; font-size: 18px; font-style: normal;
    line-height: 1.45; color: var(--ink);
  }

  /* Back */
  .card--back {
    top: 460px;
    background: var(--card-dark);
  }
  .back-brand {
    position: absolute; left: 60px; top: 50%;
    transform: translateY(-50%);
    display: flex; align-items: center; gap: 26px;
  }
  .back-brand .brand-dot { width: 96px; height: 96px; }
  .back-brand .brand-name {
    font-size: 26px; color: var(--ink-light);
  }
  .qr-space {
    position: absolute; right: 50px; top: 50%;
    transform: translateY(-50%);
    width: 110px; height: 110px; border-radius: 6px;
    border: 1.5px dashed rgba(217,217,219,0.45);
  }
</style>
</head>
<body>
  <main class="card card--front">
    <div class="faint-mark" role="img" aria-label="Faint brand mark decoration"></div>

    <header class="brand">
      <span class="brand-dot"></span>
      <p class="brand-name">Horizon Venture Methods<br>Worldwide, LLC</p>
    </header>

    <section class="person">
      <h1 class="person-name">Daniel Reyes</h1>
      <p class="person-title">Directoir</p>
    </section>

    <div class="divider"></div>

    <ul class="contacts">
      <li>
        <svg viewBox="0 0 16 16" aria-hidden="true"><path d="M4 1l3 3-2 2a9 9 0 005 5l2-2 3 3-2 3C6 15 1 10 1 3z"/></svg>
        (714) 555-0182
      </li>
      <li>
        <svg viewBox="0 0 16 16" aria-hidden="true"><rect x="1" y="5" width="14" height="8" rx="2"/><rect x="4" y="1" width="8" height="5"/></svg>
        (714) 555-0147
      </li>
      <li>
        <svg viewBox="0 0 16 16" aria-hidden="true"><path d="M1 3h14v10H1z M2 4l6 5 6-5" fill="none" stroke="#1a73c4" stroke-width="1.6"/></svg>
        info@hvmworld.example
      </li>
      <li>
        <svg viewBox="0 0 16 16" aria-hidden="true"><circle cx="8" cy="8" r="7"/></svg>
        <span>www.<span class="web-domain">hvmworld.example</span></span>
      </li>
    </ul>

    <address class="address">
      (382 W. Alder Lane,<br>Suite C, Tustin, CA 92781)
    </address>
  </main>

  <section class="card card--back">
    <div class="back-brand">
      <span class="brand-dot"></span>
      <p class="brand-name">Horizon Venture Methods<br>Worldwide, LLC</p>
    </div>
    <div class="qr-space" role="img" aria-label="Reserved space for contact QR code"></div>
  </section>
</body>
</html>
```